Web Design Project

Revamp current website adding newly designed logo and creating layout that is good on desktops, tablets, and cell phones.

Current website can be viewed at www.venkirainteriors.com

Will you see the website is small but graphics heavy in the gallery. The gallery needs to be setup so that it is easy to maintain the links and update the photos.

Needs to have high visual impact.

I need a new logo and website layout designed for my partner's business. This is a birthday present. His business is interior painting, wallpapering and design. He also has access to a wide variety of products including carpet, fabrics, furniture, wallpaper, tile, countertops, etc. I have attached some screen shots of his website for reference. He is a one man shop and has a stellar reputation with his customers. He is on-time, very tidy, excellent with animals, and always finishes on time and on budget. There are no restrictions on colors or fonts. The logo needs to work well with the website, business cards and printed materials. The website needs to flow content for device size so it looks just as good on a cell phone or tablet as it does on a desktop computer. Whatever the heck that's called! Thanks. I am looking forward to seeing everyone's ideas.

Target Market(s)

Consumers looking for interior design, painting, and wallpapering as well as interior products such as flooring, window treatments, reupholstering, counter tops, etc.

Industry/Entity Type

Cell Phone

Requirements
Must have
• Clean, sharp, visual impact (at least on the home page)
Should not have
• Clutter.

```html
<!DOCTYPE html>
<html lang="en">
<head>
<meta charset="utf-8">
<title>Venkira Interior Designs</title>
<link href="https://fonts.googleapis.com/css2?family=Lato:wght@300;400;700;900&family=PT+Serif:wght@400;700&family=Great+Vibes&display=swap" rel="stylesheet">
<style>
:root{
  --orange:#f7941d;
  --orange-deep:#e5811a;
  --ink:#2b2b33;
  --text:#444;
  --night:#241a38;
  --night-line:#3a2f52;
  --white:#fff;
  --highlight:#241a38;
}
*{margin:0;padding:0;box-sizing:border-box}
html,body{width:1200px;height:3499px;overflow:hidden;background:var(--white)}
body{position:relative;font-family:"Lato",sans-serif;color:var(--text)}
.abs{position:absolute}

/* header / hero */
.hero{left:0;top:0;width:1200px;height:752px;
  background:linear-gradient(180deg,#6f6a6c 0%,#a79a8e 28%,#c9b49b 42%,#7c6a5a 60%,#4b3c33 100%)}
.navbar{left:315px;top:63px;width:885px;height:50px;background:var(--orange);
  display:flex;align-items:center;justify-content:space-around;padding:0 20px}
.navbar a{font:400 20px "Lato",sans-serif;color:var(--ink);text-decoration:none;letter-spacing:1px}
.navbar a.active{color:var(--white)}
.logo-box{left:77px;top:0;width:238px;height:217px;background:var(--white);
  display:flex;flex-direction:column;align-items:center;justify-content:center;gap:6px}
.logo-square{width:70px;height:70px;background:var(--orange)}
.logo-name{font:400 32px "PT Serif",serif;color:var(--night);text-align:center;line-height:1.05}
.hero-title{right:62px;top:238px;text-align:right;font:900 78px/1.05 "Lato",sans-serif;color:var(--white);letter-spacing:1px}
.hero-tag{right:62px;top:428px;font:italic 400 25px "Lato",sans-serif;color:var(--orange)}
.hero-sub{right:62px;top:480px;text-align:right;font:400 34px/1.2 "Lato",sans-serif;color:var(--white)}
.thumbs{left:840px;top:612px;display:flex;gap:8px}
.thumbs span{width:88px;height:68px;border:3px solid var(--white);
  background:linear-gradient(135deg,#b7a48e,#6b5a4b)}
.dots{left:945px;top:712px;display:flex;gap:12px}
.dots i{width:12px;height:12px;border-radius:50%;background:#cfcfcf}
.dots i:first-child{background:var(--white)}

/* welcome */
.welcome-title{left:0;top:795px;width:1200px;text-align:center;font:300 54px/1.18 "Lato",sans-serif;color:var(--ink)}
.welcome-copy{left:150px;top:945px;width:900px;text-align:center;font:400 16px/1.45 "PT Serif",serif;color:var(--text)}
.welcome-copy p{margin-bottom:12px}
.welcome-copy .mark{background:var(--highlight);color:var(--white);padding:2px 4px}
.rule{left:0;top:1162px;width:1200px;height:1px;background:#ddd}

/* features */
.feature{top:1215px;width:300px;text-align:center}
.feature h3{font:400 24px "Lato",sans-serif;color:var(--ink);margin-bottom:10px}
.feature p{font:400 13px/1.35 "PT Serif",serif;color:#666;width:220px;margin:0 auto}
.feature .disc{width:212px;height:212px;border-radius:50%;background:var(--orange);
  margin:40px auto 0;display:flex;align-items:center;justify-content:center}

/* showcase */
.wave{left:0;top:1645px;width:1200px;height:30px}
.showcase{left:0;top:1662px;width:1200px;height:666px;
  background:linear-gradient(180deg,#eef1f4 0%,#c7d6e3 35%,#8fb3c9 62%,#d8e3ea 100%)}
.overlay{left:52px;top:1820px;width:396px;height:368px;background:rgba(232,150,60,.72);padding:28px 30px}
.overlay h2{font:400 64px "Great Vibes",cursive;color:var(--white);line-height:1}
.overlay p{margin-top:26px;font:400 23px/1.22 "Lato",sans-serif;color:var(--white)}
.btn{display:inline-block;margin-top:22px;background:#f4d7a8;color:var(--ink);
  font:400 24px "PT Serif",serif;padding:8px 20px}

/* portfolio */
.portfolio-title{left:0;top:2380px;width:1200px;text-align:center;font:300 52px "Lato",sans-serif;color:var(--ink)}
.portfolio-sub{left:240px;top:2460px;width:720px;text-align:center;font:400 16px/1.45 "Lato",sans-serif;color:#666}
.slide{top:2537px;height:333px}
.slide-1{left:87px;width:298px;background:linear-gradient(135deg,#3b3030,#8a7a6b 60%,#c9b8a2)}
.slide-2{left:402px;width:368px;background:linear-gradient(160deg,#ffffff 0%,#f3f3f3 30%,#d8262e 55%,#f6f6f6 80%)}
.slide-3{left:798px;width:322px;background:linear-gradient(180deg,#f4f4f4 0%,#2b3a55 22%,#e8e8e8 45%,#bfc7cf 100%)}
.picks{left:402px;top:2828px;width:368px;height:49px;background:var(--orange);
  color:var(--white);font:900 22px/49px "Lato",sans-serif;text-align:center;letter-spacing:.5px}
.arrow{top:2666px;width:44px;height:44px}

/* footer */
.footer{left:0;top:3010px;width:1200px;height:489px;background:var(--night)}
.col{top:3090px;width:180px}
.col h4{font:400 27px "Lato",sans-serif;color:var(--white);margin-bottom:22px}
.col li{list-style:none;font:400 13px "Lato",sans-serif;color:#d6d0e2;padding:12px 0;border-bottom:1px solid var(--night-line)}
.col li:first-child{border-top:1px solid var(--night-line)}
.copyright{left:94px;top:3405px;font:400 15px "Lato",sans-serif;color:var(--white)}
.copyright b{font-weight:900}
.cards{left:786px;top:3393px;display:flex;gap:14px}
.cards span{width:72px;height:40px;border-radius:6px;background:#3b5aa8;color:var(--white);
  font:700 12px/40px "Lato",sans-serif;text-align:center}
.cards span:nth-child(2){background:#d9542a}
.cards span:nth-child(3){background:#2f7fc1}
.cards span:nth-child(4){background:#2a4f9b}
</style>
</head>
<body>

<section class="abs hero" role="img" aria-label="Rooftop terrace with parasol, lounge chairs and a city skyline at sunset"></section>

<nav class="abs navbar">
  <a class="active" href="#">HOME</a>
  <a href="#">ABOUT US</a>
  <a href="#">SERVICES</a>
  <a href="#">TRAVEL REWARDS</a>
  <a href="#">CONTACT</a>
</nav>

<div class="abs logo-box">
  <div class="logo-square"></div>
  <div class="logo-name">VENKIRA<br>INTERIOR DESIGNS</div>
</div>

<h1 class="abs hero-title">KEYSTONE<br>PLACEMENT</h1>
<p class="abs hero-tag">Private Practice Audiologists And Hearing Aid Dispensers</p>
<p class="abs hero-sub">TO: PRIVATE PRACTICE<br>AUDIOLOGISTS AND HEARING AID<br>DISPENSERS</p>
<div class="abs thumbs"><span role="img" aria-label="Interior photo"></span><span role="img" aria-label="Interior photo"></span><span role="img" aria-label="Interior photo"></span></div>
<div class="abs dots"><i></i><i></i><i></i><i></i></div>

<h2 class="abs welcome-title">WELCOME TO<br>VENKIRA INTERIOR DESIGNS!</h2>
<div class="abs welcome-copy">
  <p>With the various materials, colors, and finishes available the choices today can be daunting. By listening to you, I am able to pick just the right color, the right fabric, or the right furniture for your projects.</p>
  <p><span class="mark">Whether you are starting with a small project or a large project, I am ready to bring your ideas to life. It doesn't take a big budget to achieve dramatic effects. A wonderful new look is within anyone's reach.</span></p>
  <p>My guidance with the selection of colors, fabrics, paint, wallpaper, and furniture, as well as the placement of items in a room, will help you achieve the results you desire – a beautiful home that is a joy to walk into and to show off!</p>
  <p>Your home is a reflection of your personality. Let it tell people how wonderful you are.</p>
</div>
<div class="abs rule"></div>

<div class="abs feature" style="left:182px">
  <h3>Amazing Service</h3>
  <p>Careful planning and tidy work on every visit, finished on time and on budget for each and every client we serve.</p>
  <div class="disc">
    <svg width="110" height="110" viewBox="0 0 110 110" fill="none" stroke="#fff" stroke-width="6"><rect x="15" y="15" width="80" height="80" rx="6"/><line x1="15" y1="55" x2="95" y2="55"/><line x1="42" y1="35" x2="68" y2="35"/><line x1="42" y1="75" x2="68" y2="75"/></svg>
  </div>
</div>
<div class="abs feature" style="left:448px">
  <h3>Quality &amp; Design</h3>
  <p>Fine paints, fabrics and finishes chosen with care so every room looks fresh, balanced and built to last for years.</p>
  <div class="disc">
    <svg width="110" height="110" viewBox="0 0 110 110" fill="#fff"><path d="M92 14 L100 22 L52 70 L44 62 Z"/><path d="M40 66 L48 74 C44 90 30 96 14 96 C22 88 20 74 40 66 Z"/></svg>
  </div>
</div>
<div class="abs feature" style="left:718px">
  <h3>Smooth Drive</h3>
  <p>A simple process from first visit to final touch, with clear updates so you always know what comes next in your home.</p>
  <div class="disc">
    <svg width="110" height="110" viewBox="0 0 110 110" fill="none" stroke="#fff" stroke-width="6" stroke-linejoin="round"><path d="M12 24 L40 14 L70 24 L98 14 L98 86 L70 96 L40 86 L12 96 Z"/><line x1="40" y1="14" x2="40" y2="86"/><line x1="70" y1="24" x2="70" y2="96"/></svg>
  </div>
</div>

<section class="abs showcase" role="img" aria-label="Bright modern lounge with white hanging chair, sofa and a tall window city view"></section>
<svg class="abs wave" viewBox="0 0 1200 30" preserveAspectRatio="none"><path d="M0 30 Q15 8 30 30 Q45 8 60 30 Q75 8 90 30 Q105 8 120 30 Q135 8 150 30 Q165 8 180 30 Q195 8 210 30 Q225 8 240 30 Q255 8 270 30 Q285 8 300 30 Q315 8 330 30 Q345 8 360 30 Q375 8 390 30 Q405 8 420 30 Q435 8 450 30 Q465 8 480 30 Q495 8 510 30 Q525 8 540 30 Q555 8 570 30 Q585 8 600 30 Q615 8 630 30 Q645 8 660 30 Q675 8 690 30 Q705 8 720 30 Q735 8 750 30 Q765 8 780 30 Q795 8 810 30 Q825 8 840 30 Q855 8 870 30 Q885 8 900 30 Q915 8 930 30 Q945 8 960 30 Q975 8 990 30 Q1005 8 1020 30 Q1035 8 1050 30 Q1065 8 1080 30 Q1095 8 1110 30 Q1125 8 1140 30 Q1155 8 1170 30 Q1185 8 1200 30 L1200 0 L0 0 Z" fill="#fff"/></svg>

<div class="abs overlay">
  <h2>Venkira Interiors</h2>
  <p>is a buying group / practice development group founded by audiologist owners in private practice designed for other independents in private practice</p>
  <span class="btn">READ MORE</span>
</div>

<h2 class="abs portfolio-title">OUR PORTFOLIO</h2>
<p class="abs portfolio-sub">Search for anything people, topics, hashtags, your favorite sites and then flip through articles, updates, photos and videos all in a beautiful magazine-style format.</p>

<div class="abs slide slide-1" role="img" aria-label="Tablet and phone showing a website beside stacked books"></div>
<div class="abs slide slide-2" role="img" aria-label="Website layout with a red creativity banner"></div>
<div class="abs slide slide-3" role="img" aria-label="Business website homepage layout"></div>
<div class="abs picks">AWESOME USER PICKS</div>

<svg class="abs arrow" style="left:22px" viewBox="0 0 44 44"><circle cx="22" cy="22" r="22" fill="#9b1c1c"/><path d="M26 13 L17 22 L26 31" fill="none" stroke="#fff" stroke-width="4"/></svg>
<svg class="abs arrow" style="left:1134px" viewBox="0 0 44 44"><circle cx="22" cy="22" r="22" fill="#9b1c1c"/><path d="M18 13 L27 22 L18 31" fill="none" stroke="#fff" stroke-width="4"/></svg>

<footer class="abs footer"></footer>
<div class="abs col" style="left:94px"><h4>ABOUT</h4><ul><li>About Vantelo</li><li>Terms &amp; Conditions</li><li>Privacy Policy</li><li>Track Your Order</li><li>Disclaimer</li></ul></div>
<div class="abs col" style="left:302px"><h4>NEW CARS</h4><ul><li>New Collection</li><li>Roadster (2015)</li><li>Limo Collection</li><li>Exclusive Offers</li><li>Sale</li></ul></div>
<div class="abs col" style="left:512px"><h4>FOLLOW US</h4><ul><li>Friendwall</li><li>Chirper</li><li>Snapgrid</li><li>Reelbox</li><li>Pinboardly</li></ul></div>
<div class="abs col" style="left:728px"><h4>GENERAL</h4><ul><li>Webstore</li><li>FAQ</li><li>Size Guide</li><li>Delivery &amp; Returns</li></ul></div>
<div class="abs col" style="left:946px"><h4>CONTACT</h4><ul><li>Contact</li><li>Newsletter</li></ul></div>

<p class="abs copyright">© <b>VANTELO</b> 2012-2015. ALL RIGHTS RESERVED</p>
<div class="abs cards"><span>Cardix</span><span>Paymint</span><span>Ferrus</span><span>Tallyo</span></div>

</body>
</html>
```